Business card (AI file uploaded)

We need a business card design that is minimalist using existing logo (attached). Source files must be editable so we can make the same design with other names.

Screenshots included of a design I was working on to give you an idea of the style I would like. Looking for similar modern styles

Thanks

```html
<!DOCTYPE html>
<html lang="en">
<head>
<meta charset="utf-8">
<title>Kestrel Law Group – Business Card</title>
<link rel="stylesheet" href="https://fonts.googleapis.com/css2?family=Questrial&family=Crimson+Text&display=swap">
<style>
  :root {
    --backdrop: #e4e4e4;
    --card-dark: #231f20;
    --card-light: #ffffff;
    --ink-light: #ffffff;
    --ink-dark: #1e1e1e;
    --ink-muted: #7a7a7a;
    --ink-faint: #e2e2e2;
    --shadow: rgba(0, 0, 0, 0.18);
  }
  * { margin: 0; padding: 0; box-sizing: border-box; }
  html, body {
    width: 1200px;
    height: 1200px;
    overflow: hidden;
    background: var(--backdrop);
  }
  .canvas {
    position: relative;
    width: 1200px;
    height: 1200px;
  }
  .card {
    position: absolute;
    left: 250px;
    width: 700px;
    height: 400px;
    box-shadow: 0 4px 14px var(--shadow);
  }
  .card--front {
    top: 160px;
    background: var(--card-dark);
    color: var(--ink-light);
    font-family: "Questrial", sans-serif;
    text-align: center;
  }
  .card--back {
    top: 640px;
    background: var(--card-light);
    color: var(--ink-dark);
  }

  /* Front */
  .brand-mark {
    position: absolute;
    left: 50%;
    top: 44px;
    transform: translateX(-50%);
  }
  .brand-name {
    position: absolute;
    left: 0;
    right: 0;
    top: 140px;
    font-family: "Questrial", sans-serif;
    font-weight: 400;
    color: var(--ink-light);
    line-height: 1;
  }
  .brand-name__primary {
    display: block;
    font-size: 60px;
    letter-spacing: 3px;
  }
  .brand-name__secondary {
    display: block;
    margin-top: 8px;
    font-size: 30px;
    letter-spacing: 4px;
  }
  .brand-name__suffix {
    font-size: 10px;
    letter-spacing: 1px;
  }
  .practice-areas {
    position: absolute;
    left: 0;
    right: 0;
    bottom: 40px;
    font-size: 19px;
    color: var(--ink-muted);
    letter-spacing: 0.3px;
  }

  /* Back */
  .practice-areas--back {
    position: absolute;
    left: 0;
    right: 0;
    top: 30px;
    bottom: auto;
    text-align: center;
    font-family: "Questrial", sans-serif;
    font-size: 17px;
    color: var(--ink-muted);
  }
  .practice-areas__sep { margin: 0 6px; font-size: 12px; vertical-align: 2px; }
  .watermark-mark {
    position: absolute;
    left: 168px;
    top: 72px;
  }
  .contact {
    position: absolute;
    left: 200px;
    right: 30px;
    top: 200px;
    text-align: center;
  }
  .contact__name {
    font-family: "Questrial", sans-serif;
    font-size: 32px;
    color: var(--ink-dark);
    letter-spacing: 0.5px;
  }
  .contact__title {
    font-family: "Crimson Text", serif;
    font-size: 16px;
    margin-top: 2px;
    color: var(--ink-dark);
  }
  .contact__details {
    font-family: "Crimson Text", serif;
    font-size: 19px;
    line-height: 1.3;
    margin-top: 14px;
    color: var(--ink-dark);
    font-style: normal;
  }
  .contact__phone { margin-right: 14px; }
</style>
</head>
<body>
<main class="canvas">

  <section class="card card--front" aria-label="Business card front">
    <svg class="brand-mark" width="84" height="84" viewBox="0 0 84 84" aria-hidden="true">
      <circle cx="42" cy="42" r="38" fill="none" stroke="var(--ink-light)" stroke-width="5"/>
    </svg>
    <h1 class="brand-name">
      <span class="brand-name__primary">KESTREL</span>
      <span class="brand-name__secondary">LAW GROUP<span class="brand-name__suffix"> PC</span></span>
    </h1>
    <p class="practice-areas">Real Estate | Bankruptcy | Social Security Disability</p>
  </section>

  <section class="card card--back" aria-label="Business card back">
    <p class="practice-areas--back">Real Estate<span class="practice-areas__sep">●</span>Bankruptcy<span class="practice-areas__sep">●</span>Social Security Disability</p>
    <svg class="watermark-mark" width="130" height="130" viewBox="0 0 130 130" aria-hidden="true">
      <circle cx="65" cy="65" r="60" fill="none" stroke="var(--ink-faint)" stroke-width="7"/>
    </svg>
    <div class="contact">
      <h2 class="contact__name">Jordan Kessler</h2>
      <p class="contact__title">Attorney At Law</p>
      <address class="contact__details">
        420 Meridian Ave., Suite 300, Fairhaven, IL 60999<br>
        <span class="contact__phone">P: 555.214.7730</span>F:555.214.7731<br>
        jkessler@kestrellaw.com
      </address>
    </div>
  </section>

</main>
</body>
</html>
```